Law Office Business Card

We need a business card design to include the following information:
Name of Firm: Brennick Law Group, P.A.
Address: 4627 Sandlot Ave, Ste 208, West Palm Beach, FL 33409
Phone: 561-555-0148
Fax: 561-555-0193
Website: http://www.tbrennicklaw.example

We Need a place for the Person's name and email address. Please start with the following:
Lorna K. Dwyer, Esq.
lorna@tbrennicklaw.example

```html
<!DOCTYPE html>
<html lang="en">
<head>
<meta charset="utf-8">
<title>Brennick Law Group, P.A. – Business Card</title>
<link rel="stylesheet" href="https://fonts.googleapis.com/css2?family=Montserrat:wght@400;500&display=swap">
<style>
  :root {
    --ink: #121212;
    --text: #2b2f38;
    --black: #060606;
    --navy: #262a35;
    --red: #d6003a;
    --stripe: #e6e6e6;
    --light: #e9eaec;
    --logo: #c9ccd2;
    --icon-bg: #1c0e11;
    --paper: #ffffff;
  }
  * { margin: 0; padding: 0; box-sizing: border-box; }
  html, body { width: 1200px; height: 688px; overflow: hidden; background: var(--paper); }
  .card {
    position: relative;
    width: 1200px;
    height: 688px;
    background: var(--paper);
    font-family: "Montserrat", sans-serif;
    overflow: hidden;
  }
  .card__art { position: absolute; inset: 0; width: 1200px; height: 688px; }
  .brand {
    position: absolute;
    left: 78px;
    top: 148px;
    width: 240px;
    text-align: center;
    color: var(--logo);
    font-size: 27px;
    font-weight: 400;
    line-height: 1.25;
    letter-spacing: 0.04em;
    text-transform: uppercase;
  }
  .contact-person {
    position: absolute;
    right: 54px;
    top: 46px;
    text-align: right;
    color: var(--light);
    font-size: 24px;
    font-weight: 400;
    line-height: 1.38;
  }
  .firm-name {
    position: absolute;
    left: 0;
    width: 1200px;
    top: 365px;
    text-align: center;
    color: var(--ink);
    font-size: 55px;
    font-weight: 400;
    letter-spacing: 0.005em;
  }
  .detail {
    position: absolute;
    color: var(--text);
    font-size: 26px;
    font-weight: 400;
    line-height: 1.42;
  }
  .detail--phone   { left: 218px; top: 480px; }
  .detail--web     { left: 218px; top: 564px; }
  .detail--fax     { left: 762px; top: 480px; }
  .detail--address { left: 762px; top: 538px; }
</style>
</head>
<body>
<main class="card">
  <svg class="card__art" viewBox="0 0 958 549" preserveAspectRatio="none" aria-hidden="true">
    <!-- header band -->
    <rect class="header-base" x="0" y="0" width="958" height="273" fill="var(--black)"/>
    <polygon class="header-navy" points="405,0 958,0 958,272" fill="var(--navy)"/>
    <polygon class="header-stripe" points="300,0 362,0 912,273 850,273" fill="var(--stripe)"/>
    <polygon class="header-red" points="530,114 850,273 400,273" fill="var(--red)"/>
    <polygon class="header-pointer" points="746,272 810,272 778,306" fill="var(--stripe)"/>

    <!-- footer bar -->
    <rect x="0" y="529" width="702" height="20" fill="var(--navy)"/>
    <rect x="702" y="529" width="148" height="20" fill="var(--black)"/>
    <rect x="850" y="529" width="108" height="20" fill="var(--red)"/>

    <!-- phone icon -->
    <g class="icon icon--phone">
      <circle cx="130" cy="397" r="20" fill="var(--icon-bg)"/>
      <path d="M123 387 l4 -1 l3 6 l-3 2 q2 5 6 7 l2 -3 l6 3 l-1 4 q-2 2 -5 1 q-10 -4 -13 -14 q-1 -3 1 -5z" fill="var(--red)"/>
    </g>
    <!-- web icon -->
    <g class="icon icon--web">
      <circle cx="130" cy="463" r="20" fill="var(--icon-bg)"/>
      <g stroke="var(--red)" stroke-width="2.2" fill="none" stroke-linejoin="round">
        <polyline points="117,456 126,451 139,454 143,466 136,476 122,474 117,465 117,456"/>
        <polyline points="126,451 130,463 139,454"/>
        <polyline points="117,465 130,463 143,466"/>
        <polyline points="122,474 130,463 136,476"/>
      </g>
      <g fill="var(--red)">
        <circle cx="130" cy="463" r="2.6"/><circle cx="126" cy="451" r="2.2"/>
        <circle cx="139" cy="454" r="2.2"/><circle cx="143" cy="466" r="2.2"/>
        <circle cx="136" cy="476" r="2.2"/><circle cx="122" cy="474" r="2.2"/>
        <circle cx="117" cy="456" r="2.2"/><circle cx="117" cy="465" r="2.2"/>
      </g>
    </g>
    <!-- fax / mail icon -->
    <g class="icon icon--fax">
      <circle cx="567" cy="397" r="20" fill="var(--icon-bg)"/>
      <rect x="556" y="389" width="22" height="15" fill="var(--red)"/>
      <polyline points="556,389 567,398 578,389" fill="none" stroke="var(--icon-bg)" stroke-width="1.6"/>
      <polyline points="556,404 564,396 M578,404 570,396" fill="none" stroke="var(--icon-bg)" stroke-width="1.2"/>
    </g>
    <!-- location pin -->
    <g class="icon icon--pin">
      <circle cx="567" cy="463" r="20" fill="var(--icon-bg)"/>
      <path d="M567 475 q-9 -10 -9 -16 a9 9 0 0 1 18 0 q0 6 -9 16z" fill="var(--red)"/>
    </g>
  </svg>

  <div class="brand">Brennick Law<br>Group</div>

  <div class="contact-person">
    <p class="contact-person__name">Lorna K. Dwyer, Esq.</p>
    <p class="contact-person__email">lorna@tbrennicklaw.example</p>
  </div>

  <h1 class="firm-name">Brennick Law Group, P.A.</h1>

  <p class="detail detail--phone">561-555-0148</p>
  <p class="detail detail--web">www.tbrennicklaw.example</p>
  <p class="detail detail--fax">Fax: 561-555-0193</p>
  <p class="detail detail--address">4627 Sandlot Ave, Ste 208,<br>West Palm Beach, FL 33409</p>
</main>
</body>
</html>
```